Quillfern Nightclub Flyer (Updated)

Flyer for facebook, square is fine, or rectangular. Here is the text:
QUILLFERN
Nightclub + Lounge
presents

SPLIT DECK WEDNESDAY
Nov 29 2018

CLUB FLOOR:
GORDY B2B RALPH
THEODORE BRUSKVIK

LOUNGE:
OTIS B2B HALF TIDE
COPPER FENWICK

Powered by HALVERN Acoustics
4716 Larchmere Avenue 21+ 9pm-2am
quillfernvenue-example.com for VIP booth inquiries

Target Market(s)

Nightclub

Industry/Entity Type

Night Club

Font styles to use
Sans Serif

Colors

Designer to choose colors to be used in the design.

Requirements
Must have
• All the text listed, and plz keep the theme of the attached files. We want to stay consistent with the Quillfern brand
Nice to have
• Try to stay with the theme from the attachments
Should not have
• Dont' stray to far from the general theme we have from the attachments

```html
<!DOCTYPE html>
<html lang="en">
<head>
<meta charset="utf-8">
<title>Quillfern Nightclub – Split Deck Wednesday</title>
<link rel="stylesheet" href="https://fonts.googleapis.com/css2?family=Playfair+Display:wght@400&family=Montserrat:wght@400;500;700;800&family=Lato:wght@400&display=swap">
<style>
  :root {
    --blush: #fbf1ef;
    --blush-deep: #f1e2df;
    --ink: #2b2a29;
    --gold-light: #d6a21e;
    --gold-dark: #a27a4a;
    --rule-grey: #cfcfcf;
    --white: #ffffff;
  }
  * { margin: 0; padding: 0; box-sizing: border-box; }
  html, body { width: 1200px; height: 1200px; overflow: hidden; background: var(--blush); }
  .flyer {
    position: relative;
    width: 1200px;
    height: 1200px;
    background: var(--blush);
    color: var(--ink);
    font-family: "Montserrat", sans-serif;
    overflow: hidden;
  }
  .backdrop-pattern {
    position: absolute; inset: 0;
    background:
      radial-gradient(circle at 28% 48%, var(--blush-deep) 0, rgba(241,226,223,0) 42%),
      radial-gradient(circle at 80% 30%, rgba(241,226,223,0.7) 0, rgba(241,226,223,0) 35%),
      var(--blush);
  }
  .frame { position: absolute; inset: 0; }
  .line { position: absolute; left: 0; width: 1200px; text-align: center; white-space: nowrap; }
  .venue-name {
    top: 168px;
    font-family: "Playfair Display", serif;
    font-weight: 400;
    font-size: 96px; line-height: 1;
    letter-spacing: 1px;
  }
  .venue-tagline {
    top: 288px;
    font-family: "Lato", sans-serif;
    font-size: 27px; line-height: 1; letter-spacing: 3px;
  }
  .venue-presents {
    top: 326px;
    font-family: "Lato", sans-serif;
    font-size: 15px; line-height: 1; letter-spacing: 4px;
  }
  .divider {
    position: absolute; top: 362px; left: 507px; width: 186px; height: 2px;
    background: linear-gradient(90deg, var(--gold-dark), var(--gold-light));
    opacity: 0.8;
  }
  .event-title {
    top: 412px;
    font-weight: 700; font-size: 37px; line-height: 1; letter-spacing: 7px;
  }
  .event-date {
    top: 465px;
    font-family: "Lato", sans-serif;
    font-size: 31px; line-height: 1;
  }
  .room-badge {
    position: absolute; left: 50%; transform: translateX(-50%);
    height: 39px; padding: 0 17px;
    background: linear-gradient(90deg, var(--gold-dark), var(--gold-light));
    color: var(--white);
    font-weight: 800; font-size: 24px; letter-spacing: 3px; line-height: 39px;
    white-space: nowrap;
  }
  .room-club { top: 550px; }
  .room-lounge { top: 711px; }
  .act-pair { font-size: 24px; line-height: 1; letter-spacing: 0.5px; }
  .act-headliner { font-size: 32px; line-height: 1; letter-spacing: 1px; }
  .club-pair { top: 611px; }
  .club-headliner { top: 641px; }
  .lounge-pair { top: 775px; }
  .lounge-headliner { top: 804px; }
  .powered-label {
    top: 900px; font-size: 16px; line-height: 1; letter-spacing: 3px;
  }
  .sponsor-rule {
    position: absolute; top: 949px; width: 110px; height: 2px;
  }
  .sponsor-rule.left { left: 272px; background: linear-gradient(90deg, rgba(162,122,74,0), var(--gold-dark)); }
  .sponsor-rule.right { left: 818px; background: linear-gradient(90deg, var(--gold-dark), rgba(162,122,74,0)); }
  .sponsor-name {
    top: 934px; font-weight: 800; font-size: 30px; line-height: 1; letter-spacing: 2px;
  }
  .venue-details {
    top: 997px; font-size: 23px; line-height: 26px; letter-spacing: 0.5px;
  }
</style>
</head>
<body>
<main class="flyer">
  <div class="backdrop-pattern" role="img" aria-label="Faint blush floral pattern with a large soft brand emblem in the background"></div>

  <svg class="frame" width="1200" height="1200" viewBox="0 0 1200 1200" aria-hidden="true">
    <defs>
      <linearGradient id="frameGold" x1="0" y1="0" x2="1" y2="1">
        <stop offset="0" stop-color="#d6a21e"/>
        <stop offset="0.5" stop-color="#a27a4a"/>
        <stop offset="1" stop-color="#d6a21e"/>
      </linearGradient>
    </defs>
    <rect x="117" y="117" width="968" height="968" fill="none" stroke="#cfcfcf" stroke-width="1.5"/>
    <path d="M143 86 H1056 V145 H1114 V1056 H1056 V1114 H143 V1056 H86 V145 H143 Z"
          fill="none" stroke="url(#frameGold)" stroke-width="5"/>
  </svg>

  <h1 class="line venue-name">QUILLFERN</h1>
  <p class="line venue-tagline">NIGHTCLUB + LOUNGE</p>
  <p class="line venue-presents">PRESENTS</p>
  <div class="divider"></div>

  <h2 class="line event-title">SPLIT DECK WEDNESDAY</h2>
  <p class="line event-date">Nov 29 2018</p>

  <div class="room-badge room-club">CLUB FLOOR</div>
  <p class="line act-pair club-pair">GORDY B2B RALPH</p>
  <p class="line act-headliner club-headliner">THEODORE BRUSKVIK</p>

  <div class="room-badge room-lounge">LOUNGE</div>
  <p class="line act-pair lounge-pair">OTIS B2B HALF TIDE</p>
  <p class="line act-headliner lounge-headliner">COPPER FENWICK</p>

  <p class="line powered-label">POWERED BY</p>
  <div class="sponsor-rule left"></div>
  <p class="line sponsor-name">HALVERN ACOUSTICS</p>
  <div class="sponsor-rule right"></div>

  <p class="line venue-details">4716 Larchmere Avenue 21+ 9pm-2am<br>quillfernvenue-example.com For VIP booth inquiries</p>
</main>
</body>
</html>
```